Dorvelan Swimming & Athletics Center

We need Business Card for a Athletics center
The logo frome the Uploaded Files ( b card fimal)
Οn one side of card we need the logo of company the Contact and the website:
1. Address:(Limassol, Cyprus 12-14 Stavrinelou str,Ano Trimeni,P.C. 4832)

2.Phone number: (+357) 25-704263

3. Mail: info@dorvelanfit.example

3. Website: www.dorvelanfit.example

Οn the other side of the card we need to write the sport of the company:

1. Artistic Gymnastics
2. Swimming
3. Gym - Fitness
4. Programs
5. Dancing
5.Tennis

From the Uploaded Files you can get the logo.In a logo is behind the black color which can be removed from logo.

Υou can use that color you want.
.
Updates

Industry/Entity Type

Business

Font styles to use
Decorative

Colors
0555a3
ffcf3e
3176b5
0692cd
add136
f04a50
000000
cfcfcf
9d9d9d

Requirements
Should not have
• photos with faces
• photo fro the Website:www.dorvelanfit.example

```html
<!DOCTYPE html>
<html lang="en">
<head>
<meta charset="utf-8">
<title>Dorvelan Swimming &amp; Athletics Center – Business Card</title>
<link href="https://fonts.googleapis.com/css2?family=Saira+Stencil+One&family=Stardos+Stencil:wght@400;700&display=swap" rel="stylesheet">
<style>
  :root {
    --bg: #c4c3c0;
    --card: #161616;
    --orange: #f2a325;
    --white: #f4f4f4;
    --grey: #9d9d9d;
    --light-grey: #cfcfcf;
  }
  * { box-sizing: border-box; margin: 0; padding: 0; }
  html, body { width: 1200px; height: 1000px; overflow: hidden; }
  body {
    background: radial-gradient(ellipse at 50% 45%, #d6d5d2 0%, var(--bg) 60%, #a9a8a5 100%);
    position: relative;
    font-family: "Stardos Stencil", sans-serif;
  }
  .card {
    position: absolute;
    top: 345px;
    width: 540px;
    height: 310px;
    background: var(--card);
    box-shadow: 0 14px 30px rgba(0,0,0,.35);
    overflow: hidden;
  }
  .card--front { left: 30px; }
  .card--back { left: 630px; background: linear-gradient(135deg, #222 0%, var(--card) 55%, #101010 100%); }

  .splatter { position: absolute; }
  .splatter--top-left {
    left: 0; top: 0; width: 120px; height: 230px;
    background: radial-gradient(ellipse at 20% 30%, rgba(242,163,37,.7) 0%, rgba(207,207,207,.25) 45%, transparent 75%);
  }
  .splatter--top-right {
    right: 0; top: 20px; width: 110px; height: 220px;
    background: radial-gradient(ellipse at 70% 40%, rgba(207,207,207,.55) 0%, rgba(242,163,37,.35) 45%, transparent 75%);
  }
  .splatter--bottom {
    left: 150px; bottom: 0; width: 110px; height: 30px;
    background: radial-gradient(ellipse at 50% 100%, rgba(207,207,207,.45) 0%, transparent 70%);
  }

  .brand { position: absolute; left: 0; right: 0; top: 42px; text-align: center; }
  .brand__mark {
    display: block; width: 68px; height: 68px; margin: 0 auto 18px;
    border-radius: 50%; background: #1e1e1e; border: 4px solid var(--orange);
  }
  .brand__name {
    font-family: "Saira Stencil One", sans-serif;
    font-size: 74px; line-height: 1; letter-spacing: 1px;
    color: var(--orange);
  }

  .address { position: absolute; left: 20px; top: 238px; display: flex; gap: 14px; align-items: flex-start; }
  .address__text { color: var(--orange); font-size: 11px; line-height: 1.6; text-transform: uppercase; padding-top: 2px; }

  .contacts { position: absolute; left: 334px; top: 206px; list-style: none; }
  .contacts li { display: flex; align-items: center; gap: 14px; height: 30px; color: var(--orange); font-size: 13px; font-weight: 400; white-space: nowrap; }
  .contacts svg { width: 22px; height: 22px; flex: none; }

  .frame {
    position: absolute; inset: 14px 12px;
    border: 5px solid var(--orange);
  }
  .sports { position: absolute; left: 84px; top: 50px; list-style: none; }
  .sports li {
    display: flex; align-items: center; gap: 10px;
    font-family: "Saira Stencil One", sans-serif;
    font-size: 24px; line-height: 34px; color: var(--white); text-transform: uppercase;
    white-space: nowrap;
  }
  .sports svg { width: 22px; height: 22px; flex: none; }
  .sport-art {
    position: absolute; right: 28px; top: 36px; width: 110px; height: 240px;
    background: radial-gradient(ellipse at 55% 55%, rgba(207,207,207,.55) 0%, rgba(157,157,157,.3) 40%, rgba(242,163,37,.15) 65%, transparent 80%);
  }
</style>
</head>
<body>
  <section class="card card--front" aria-label="Card front">
    <div class="splatter splatter--top-left" role="img" aria-label="Orange and white paint splatter"></div>
    <div class="splatter splatter--top-right" role="img" aria-label="White and orange paint splatter"></div>
    <div class="splatter splatter--bottom" role="img" aria-label="White paint splatter"></div>

    <div class="brand">
      <span class="brand__mark"></span>
      <h1 class="brand__name">DORVELAN</h1>
    </div>

    <div class="address">
      <svg width="26" height="36" viewBox="0 0 26 36" aria-hidden="true">
        <path d="M13 0C5.8 0 0 5.6 0 12.6 0 22 13 36 13 36s13-14 13-23.4C26 5.6 20.2 0 13 0z" fill="var(--orange)"/>
        <circle cx="13" cy="12.5" r="5" fill="var(--card)"/>
      </svg>
      <p class="address__text">Limassol, Cyprus 12-14 Stavrinelou str.<br>Ano Trimeni,<br>P.C. 4832</p>
    </div>

    <ul class="contacts">
      <li>
        <svg viewBox="0 0 24 24" aria-hidden="true"><path d="M6.6 10.8a15.1 15.1 0 0 0 6.6 6.6l2.2-2.2c.3-.3.7-.4 1-.2 1.1.4 2.3.6 3.6.6.6 0 1 .4 1 1V20c0 .6-.4 1-1 1A17 17 0 0 1 3 4c0-.6.4-1 1-1h3.5c.6 0 1 .4 1 1 0 1.3.2 2.5.6 3.6.1.3 0 .7-.2 1z" fill="var(--orange)"/></svg>
        (+357) 25-704263
      </li>
      <li>
        <svg viewBox="0 0 24 24" aria-hidden="true"><text x="12" y="19" text-anchor="middle" font-size="22" font-weight="700" fill="var(--orange)" font-family="sans-serif">@</text></svg>
        info@dorvelanfit.example
      </li>
      <li>
        <svg viewBox="0 0 24 24" aria-hidden="true" fill="none" stroke="var(--orange)" stroke-width="1.8"><circle cx="12" cy="12" r="10"/><ellipse cx="12" cy="12" rx="4.5" ry="10"/><path d="M2 12h20M4 6.5h16M4 17.5h16"/></svg>
        www.dorvelanfit.example
      </li>
    </ul>
  </section>

  <section class="card card--back" aria-label="Card back">
    <div class="frame"></div>
    <ul class="sports">
      <li><svg viewBox="0 0 24 24" aria-hidden="true"><path d="M12 1l3.1 7.2 7.8.7-5.9 5.2 1.8 7.6L12 17.8 5.2 21.7 7 14.1 1.1 8.9l7.8-.7z" fill="var(--white)"/></svg>Artistic Gymnastics</li>
      <li><svg viewBox="0 0 24 24" aria-hidden="true"><path d="M12 1l3.1 7.2 7.8.7-5.9 5.2 1.8 7.6L12 17.8 5.2 21.7 7 14.1 1.1 8.9l7.8-.7z" fill="var(--white)"/></svg>Swimming</li>
      <li><svg viewBox="0 0 24 24" aria-hidden="true"><path d="M12 1l3.1 7.2 7.8.7-5.9 5.2 1.8 7.6L12 17.8 5.2 21.7 7 14.1 1.1 8.9l7.8-.7z" fill="var(--white)"/></svg>Gym-Fitness</li>
      <li><svg viewBox="0 0 24 24" aria-hidden="true"><path d="M12 1l3.1 7.2 7.8.7-5.9 5.2 1.8 7.6L12 17.8 5.2 21.7 7 14.1 1.1 8.9l7.8-.7z" fill="var(--white)"/></svg>Programs</li>
      <li><svg viewBox="0 0 24 24" aria-hidden="true"><path d="M12 1l3.1 7.2 7.8.7-5.9 5.2 1.8 7.6L12 17.8 5.2 21.7 7 14.1 1.1 8.9l7.8-.7z" fill="var(--white)"/></svg>Dancing</li>
      <li><svg viewBox="0 0 24 24" aria-hidden="true"><path d="M12 1l3.1 7.2 7.8.7-5.9 5.2 1.8 7.6L12 17.8 5.2 21.7 7 14.1 1.1 8.9l7.8-.7z" fill="var(--white)"/></svg>Tennis</li>
    </ul>
    <div class="sport-art" role="img" aria-label="Sports illustration: silhouettes of a gymnast and a seated figure, a tennis racket, a checkered flag and stars"></div>
  </section>
</body>
</html>
```